Artificial Intelligence and Machine Learning Company Needs a New Website

We need a new web design for one of the leading companies in the Spanish market in the development of advanced analytics and artificial intelligence.
Our goal is to help in resolving complex planning decisions and improving the operational efficiency of our clients. We have big clients from different industries and very powerful technology partners. We want our new website to be clear and show our great experience in the sector (more than 10 years) and our young spirit.
Number of Pages Required
5+ page
Colors
Designer to choose colors to be used in the design.
Look and feel

```html
<!DOCTYPE html>
<html lang="en">
<head>
<meta charset="utf-8">
<title>Resolva – Planning, Optimization, Decision Management</title>
<link href="https://fonts.googleapis.com/css2?family=Ubuntu:ital,wght@0,300;0,400;0,500;0,700;1,400&family=Open+Sans:ital,wght@0,400;0,600;0,700;1,400&display=swap" rel="stylesheet">
<style>
:root{
  --red:#e0401a;
  --orange:#ee5b20;
  --purple:#a80aaa;
  --magenta:#b00bb0;
  --ink:#222;
  --muted:#555;
  --card-grey:#dedede;
  --tech-bg:#ececec;
  --peach:#fde4d8;
  --band:#dc3c18;
  --pink:#f7e8f4;
  --white:#fff;
  --dark:#111;
}
*{box-sizing:border-box;margin:0;padding:0}
html,body{width:1200px;height:5021px;overflow:hidden;background:var(--white)}
body{font-family:"Open Sans",sans-serif;color:var(--ink)}
.page{position:relative;width:1200px;height:5021px;overflow:hidden}
.abs{position:absolute}
.heading{font-family:"Ubuntu",sans-serif}

/* hero */
.hero{position:absolute;left:0;top:0;width:1200px;height:700px;
  background:radial-gradient(ellipse at 62% 30%,#6b5a55 0%,#3a2f33 35%,#1d1a22 70%,#120f16 100%)}
.hero-tear{position:absolute;left:0;top:0}
.topbar{position:absolute;top:26px;right:74px;display:flex;align-items:center;gap:14px;color:#fff;font-family:"Ubuntu",sans-serif;font-weight:500;font-size:19px}
.social-dot{width:11px;height:11px;border-radius:50%;background:#fff;display:inline-block}
.sep{opacity:.7;margin:0 4px}
.phone{display:flex;align-items:center;gap:6px}
.brand{position:absolute;display:flex;align-items:center;gap:10px;font-family:"Ubuntu",sans-serif;font-weight:500;color:var(--red)}
.brand-dot{border-radius:50%;background:var(--purple)}
.nav{position:absolute;left:432px;top:74px;width:694px;height:40px;border-radius:20px;background:var(--red);display:flex;align-items:center;padding-left:36px;gap:0}
.nav a{color:#fff;text-decoration:none;font-size:11.5px;font-weight:600;padding:0 14px;line-height:40px}
.nav a.active{background:#2a2225;height:40px}
.hero-title{position:absolute;left:72px;top:305px;font-family:"Ubuntu",sans-serif;font-weight:700;font-size:50px;line-height:58px;color:var(--orange)}
.hero-sub{position:absolute;left:76px;top:428px;color:#fff;font-size:22px;font-weight:400}
.pill{position:absolute;border-radius:24px;color:#fff;font-weight:700;display:flex;align-items:center;justify-content:center;text-decoration:none}
.hero-dots{position:absolute;left:566px;top:550px;display:flex;gap:12px}
.hero-dots span{width:6px;height:6px;border-radius:50%;background:#fff}

/* intro */
.intro-col{position:absolute;top:760px;width:480px}
.intro-col .ico{width:100px;height:104px}
.intro-col h2{font-family:"Ubuntu",sans-serif;font-weight:500;font-size:25px;margin-top:36px}
.intro-col p{font-size:15.5px;line-height:33px;margin-top:22px;color:#333}

/* areas */
.areas{position:absolute;left:0;top:1210px;width:1200px;height:1090px;background:var(--magenta)}
.section-title{position:absolute;left:0;width:1200px;text-align:center;font-family:"Ubuntu",sans-serif;font-size:42px}
.area-grid{position:absolute;left:72px;top:259px;display:grid;grid-template-columns:repeat(4,259px);grid-auto-rows:344px;gap:9px 7px}
.area-card{background:var(--card-grey)}
.area-photo{height:226px}
.area-label{height:118px;display:flex;align-items:center;justify-content:center;text-align:center;font-family:"Ubuntu",sans-serif;font-weight:500;font-size:22px;line-height:33px;color:#222}

/* how we work */
.how{position:absolute;left:0;top:2299px;width:1200px;height:840px;background:var(--orange)}
.step{position:absolute;top:196px;width:228px;color:#fff}
.step .num{font-family:"Ubuntu",sans-serif;font-weight:500;font-size:40px;line-height:44px}
.step h3{font-family:"Ubuntu",sans-serif;font-weight:700;font-size:20px;margin-top:10px}
.step .price{font-style:italic;font-size:18px;margin-top:8px;opacity:.95}
.step .days{font-family:"Ubuntu",sans-serif;font-weight:700;font-size:20px;margin-top:9px}
.step p{font-size:12.5px;line-height:22px;text-align:justify;margin-top:18px}

/* testimonial */
.quote{position:absolute;left:258px;top:3170px;width:684px;text-align:center;font-size:13px;line-height:22px;color:#333}
.arrow{position:absolute;top:3246px}
.person{position:absolute;left:0;width:1200px;text-align:center}

/* technologies */
.tech{position:absolute;left:0;top:3541px;width:1200px;height:663px;background:var(--tech-bg)}
.tech-card{position:absolute;top:147px;width:170px;height:412px;border-radius:14px;text-align:center;padding-top:36px}
.tech-card.peach{background:var(--peach)}
.tech-card.white{background:#fff}
.tech-icon{width:78px;height:70px;margin:0 auto;border-radius:8px}
.tech-card h4{font-family:"Ubuntu",sans-serif;font-weight:500;font-size:19px;line-height:28px;margin-top:38px;color:#222}
.tech-card p{font-size:11.5px;line-height:22px;color:#444;margin:16px 16px 0}
.go{width:24px;height:24px;border-radius:50%;background:var(--red);margin:22px auto 0;display:flex;align-items:center;justify-content:center}

/* partners */
.partners{position:absolute;left:0;top:4204px;width:1200px;height:230px;background:var(--band)}
.badge{position:absolute;background:rgba(255,255,255,.92)}

/* contact */
.contact{position:absolute;left:0;top:4434px;width:1200px;height:520px;background:var(--pink)}
.contact-item{position:absolute;top:170px;display:flex;align-items:center;gap:16px;font-family:"Ubuntu",sans-serif;font-weight:500;font-size:22px;color:#222}
.links-title{position:absolute;font-family:"Ubuntu",sans-serif;font-weight:700;font-size:27px;color:#222}
.links{position:absolute;list-style:none;font-size:16.5px;line-height:27.5px;color:#222}
.links li::before{content:"›";font-weight:700;margin-right:22px}
.follow{position:absolute;left:922px;top:360px;display:flex;gap:38px}
.follow span{width:20px;height:20px;border-radius:50%;background:#222}
.footer{position:absolute;left:0;top:4954px;width:1200px;height:67px;background:var(--dark);color:#fff;font-size:14px;display:flex;align-items:center;justify-content:center}
.footer .tag{position:absolute;right:24px;font-size:12px;opacity:.8}
</style>
</head>
<body>
<div class="page">

  <!-- HERO -->
  <section class="hero" role="img" aria-label="Person wearing a virtual reality headset reaching out into a blurred night city scene"></section>
  <svg class="hero-tear" width="1200" height="700" viewBox="0 0 1200 700" aria-hidden="true">
    <polygon fill="#fff" points="0,700 0,690 30,684 52,672 88,680 120,660 160,664 196,646 230,650 266,634 300,640 340,620 372,626 408,608 446,612 480,596 516,600 552,584 590,590 626,572 662,576 700,560 736,566 772,550 808,553 846,538 880,542 918,526 954,530 990,516 1028,520 1062,508 1100,512 1136,500 1170,504 1200,494 1200,700"/>
  </svg>

  <div class="topbar">
    <span class="social-dot"></span><span class="social-dot"></span><span class="social-dot"></span><span class="social-dot"></span>
    <span class="sep">|</span>
    <span class="phone">
      <svg width="14" height="14" viewBox="0 0 24 24"><path fill="#fff" d="M6.6 10.8a15 15 0 0 0 6.6 6.6l2.2-2.2c.3-.3.7-.4 1-.2 1.1.4 2.3.6 3.6.6.6 0 1 .4 1 1V20c0 .6-.4 1-1 1C10.6 21 3 13.4 3 4c0-.6.4-1 1-1h3.5c.6 0 1 .4 1 1 0 1.3.2 2.5.6 3.6.1.3 0 .7-.2 1z"/></svg>
      1-800 555 0142
    </span>
  </div>

  <div class="brand" style="left:74px;top:54px;font-size:54px">Resolva<span class="brand-dot" style="width:30px;height:30px"></span></div>

  <nav class="nav">
    <a class="active">Home</a><a>About Us</a><a>Industries</a><a>How we work</a><a>Testimonials</a><a>Technologies</a><a>Contact Us</a>
  </nav>

  <h1 class="hero-title">Planning , Optimization,<br>decision management</h1>
  <p class="hero-sub">Advanced Analytics and Artificial Intelligence for smart decisions</p>
  <a class="pill" style="left:72px;top:490px;width:240px;height:44px;background:var(--purple);font-size:17px">Interested to join us?</a>
  <div class="hero-dots"><span></span><span></span><span></span><span></span></div>

  <!-- INTRO -->
  <div class="intro-col" style="left:74px">
    <div class="ico" role="img" aria-label="Small illustration of a manager above an organisation chart" style="background:linear-gradient(180deg,#2f3e5c 0%,#2f3e5c 55%,#e05a3a 80%,#7bc47f 100%);border-radius:6px;width:86px"></div>
    <h2>What We do</h2>
    <p>Resolva AI implements AI based solutions for supply chain planning &amp; optimization, workforce optimization and rule based decision management</p>
    <a class="pill" style="position:relative;margin-top:26px;width:184px;height:58px;background:var(--red);font-size:17px;border-radius:30px">Read more</a>
  </div>
  <div class="intro-col" style="left:618px;width:490px">
    <div class="ico" role="img" aria-label="Small illustration of a magnifying glass over a person" style="background:linear-gradient(135deg,#dbe6f2 0%,#9fb6d0 50%,#2f3e5c 100%);border-radius:50% 50% 50% 8px;width:104px"></div>
    <h2>Who we are</h2>
    <p>We consider ourselves the experts in mathematical and rule based decision management. 15 years in business and many successful projects make that we can say this without the risk of disappointing you. we have carefully selected the world's est in class software supplies as partners to work with.</p>
    <a class="pill" style="position:relative;margin-top:26px;width:184px;height:58px;background:var(--purple);font-size:17px;border-radius:30px">Read more</a>
  </div>

  <!-- AREAS -->
  <section class="areas">
    <svg class="abs" style="left:0;top:0" width="1200" height="70" viewBox="0 0 1200 70" aria-hidden="true">
      <polygon fill="#fff" points="0,0 1200,0 1200,56 1168,50 1130,60 1092,52 1056,62 1018,50 980,58 944,48 904,60 866,50 828,58 790,46 752,56 716,48 676,58 640,44 600,54 560,46 522,56 486,40 448,50 410,38 372,48 334,36 296,44 258,32 220,40 184,28 146,36 110,22 72,32 36,18 0,26"/>
    </svg>
    <h2 class="section-title" style="top:170px;color:#fff"><b style="font-weight:700">AREAS &amp;</b> <span style="font-weight:300">INDUSTRIES</span></h2>
    <div class="area-grid">
      <div class="area-card"><div class="area-photo" role="img" aria-label="Field technician in a hard hat working on machinery" style="background:linear-gradient(135deg,#9ab4cc,#3f5f86 60%,#1f2e44)"></div><div class="area-label">FIELD SERVICES</div></div>
      <div class="area-card"><div class="area-photo" role="img" aria-label="Hands sheltering a paper cut-out family and house" style="background:linear-gradient(180deg,#2b2b2b,#6a6a6a 60%,#cfcfcf)"></div><div class="area-label">INSURANCE</div></div>
      <div class="area-card"><div class="area-photo" role="img" aria-label="Cargo plane over trucks and containers at sunset" style="background:linear-gradient(180deg,#f2c98a,#d98646 50%,#5a4a52)"></div><div class="area-label">TRANSPORTATION<br>&amp; LOGISTICS</div></div>
      <div class="area-card"><div class="area-photo" role="img" aria-label="Worker in a safety vest pointing at warehouse shelves" style="background:linear-gradient(135deg,#e8b43c,#8a5a2e 55%,#2c2a3a)"></div><div class="area-label">WORKFORCE<br>PLANNING</div></div>
      <div class="area-card"><div class="area-photo" role="img" aria-label="Engineer with a tablet in a manufacturing plant" style="background:linear-gradient(135deg,#4f9cb8,#2f5f7a 55%,#c87a3a)"></div><div class="area-label">MANUFACTURING</div></div>
      <div class="area-card"><div class="area-photo" role="img" aria-label="Close-up of an aircraft jet engine" style="background:linear-gradient(135deg,#d8d8d8,#7a7a7a 50%,#2a2a2a)"></div><div class="area-label">AVIATION</div></div>
      <div class="area-card"><div class="area-photo" role="img" aria-label="Shoppers using an orange self-service kiosk" style="background:linear-gradient(135deg,#f6a15a,#e8702a 50%,#7b5a4e)"></div><div class="area-label">RETAIL</div></div>
      <div class="area-card"><div class="area-photo" role="img" aria-label="People reviewing documents with a laptop at a desk" style="background:linear-gradient(135deg,#e9e6e2,#b8b0a8 55%,#4a5468)"></div><div class="area-label">BANKING</div></div>
    </div>
  </section>

  <!-- HOW WE WORK -->
  <section class="how">
    <h2 class="section-title" style="top:64px;color:#fff;font-weight:700">HOW WE WORK</h2>
    <div class="step" style="left:76px">
      <div class="num">01</div><h3>Initial analysis</h3><div class="price">Free of charge</div><div class="days">0.5 - 1 day</div>
      <p>Together we analyse the Lorem ipsum dolor sit amet, consectetur adipiscing elit, sed do eiusmod tempor incididunt ut labore et dolore magna aliqua. Ut enim ad minim veniam, quis nostrud exercitation ullamco laboris nisi ut aliquip ex ea commodo consequat. Duis aute irure dolor in reprehenderit in voluptate velit</p>
    </div>
    <div class="step" style="left:348px">
      <div class="num">02</div><h3>Scan</h3><div class="price">We only charge 50%</div><div class="days">2 - 5 day</div>
      <p>Our consultation conduct Lorem ipsum dolor sit amet, consectetur adipiscing elit, sed do eiusmod tempor incididunt ut labore et dolore magna aliqua. Ut enim ad minim veniam, quis nostrud exercitation ullamco laboris nisi ut aliquip ex ea commodo consequat. Duis aute irure dolor in reprehenderit in voluptate velit</p>
    </div>
    <div class="step" style="left:620px">
      <div class="num">03</div><h3>Prototype</h3><div class="price">We Only charge 75%</div><div class="days">5 - 15 day</div>
      <p>Based on your data Lorem ipsum dolor sit amet, consectetur adipiscing elit, sed do eiusmod tempor incididunt ut labore et dolore magna aliqua. Ut enim ad minim veniam, quis nostrud exercitation ullamco laboris nisi ut aliquip ex ea commodo consequat. Duis aute irure dolor in reprehenderit in voluptate velit</p>
    </div>
    <div class="step" style="left:891px">
      <div class="num">04</div><h3>Project</h3>
      <p style="margin-top:70px">Execution of the project development and implementation Lorem ipsum dolor sit amet, consectetur adipiscing elit, sed do eiusmod tempor incididunt ut labore et dolore magna aliqua. Ut enim ad minim veniam,</p>
    </div>
    <svg class="abs" style="left:0;top:600px" width="1200" height="240" viewBox="0 0 1200 240" aria-hidden="true">
      <polygon fill="#fff" points="0,222 34,210 70,216 104,198 140,204 176,186 212,192 248,174 284,178 318,162 356,168 390,150 426,154 462,140 500,144 534,126 570,130 606,114 642,120 678,102 714,106 750,90 788,94 822,78 858,82 894,64 930,68 966,52 1004,56 1038,40 1074,44 1110,30 1146,34 1180,22 1200,24 1200,240 0,240"/>
    </svg>
  </section>

  <!-- TESTIMONIAL -->
  <p class="quote">“Resolva has Proven to be a reliable company with highly qualified Lorem ipsum dolor sit amet, consectetur adipiscing elit, sed do eiusmod tempor incididunt ut labore et dolore magna aliqua. Ut enim ad minim veniam, quis nostrud exercitation ullamco laboris nisi ut aliquip ex ea commodo consequat. Duis aute irure dolor in reprehenderit in voluptate velit”</p>
  <svg class="arrow" style="left:134px" width="14" height="22" viewBox="0 0 14 22" aria-label="Previous"><path d="M12 2 3 11l9 9" fill="none" stroke="#222" stroke-width="3"/></svg>
  <svg class="arrow" style="left:1040px" width="14" height="22" viewBox="0 0 14 22" aria-label="Next"><path d="M2 2l9 9-9 9" fill="none" stroke="#222" stroke-width="3"/></svg>
  <div class="person heading" style="top:3288px;font-weight:500;font-size:21px">Lucas Ferrer Vidal</div>
  <div class="person" style="top:3322px;font-style:italic;font-size:13px;color:#444">Head of the operations applications department at Norvia Grid</div>
  <a class="pill" style="left:493px;top:3372px;width:212px;height:56px;background:var(--red);font-size:17px;border-radius:28px">Success Stories</a>

  <!-- TECHNOLOGIES -->
  <section class="tech">
    <h2 class="section-title" style="top:50px;color:#111;font-weight:700">TECHNOLOGIES</h2>
    <div class="tech-card peach" style="left:74px"><div class="tech-icon" role="img" aria-label="Icon of a monitor showing a chart" style="background:linear-gradient(180deg,#c9d9ec,#5e7ea6)"></div><h4>Advanced<br>analytics</h4><p>Find out how we use predictive and prescriptive analytics to improve business performance</p><div class="go"><svg width="8" height="10" viewBox="0 0 8 10"><path d="M2 1l4 4-4 4" stroke="#fff" stroke-width="2" fill="none"/></svg></div></div>
    <div class="tech-card white" style="left:251px"><div class="tech-icon" role="img" aria-label="Icon of a robot" style="background:linear-gradient(180deg,#e2e2e2,#8a8a8a)"></div><h4>Artificial<br>Intelligence</h4><p>Find out how we use predictive and prescriptive analytics to improve business performance</p><div class="go"><svg width="8" height="10" viewBox="0 0 8 10"><path d="M2 1l4 4-4 4" stroke="#fff" stroke-width="2" fill="none"/></svg></div></div>
    <div class="tech-card peach" style="left:428px"><div class="tech-icon" role="img" aria-label="Icon of a rules checklist" style="background:linear-gradient(180deg,#f2c0b8,#3c7fd0)"></div><h4>Rule-based<br>systems</h4><p>Find out how we use predictive and prescriptive analytics to improve business performance</p><div class="go"><svg width="8" height="10" viewBox="0 0 8 10"><path d="M2 1l4 4-4 4" stroke="#fff" stroke-width="2" fill="none"/></svg></div></div>
    <div class="tech-card white" style="left:605px"><div class="tech-icon" role="img" aria-label="Icon of a head with connected gears" style="background:linear-gradient(180deg,#f2c24a,#4d6ea8)"></div><h4>Machine<br>Learning</h4><p>Find out how we use predictive and prescriptive analytics to improve business performance</p><div class="go"><svg width="8" height="10" viewBox="0 0 8 10"><path d="M2 1l4 4-4 4" stroke="#fff" stroke-width="2" fill="none"/></svg></div></div>
    <div class="tech-card peach" style="left:782px"><div class="tech-icon" role="img" aria-label="Icon of a calculator" style="background:linear-gradient(180deg,#f6c23c,#f3a33a)"></div><h4>Mathematical<br>Optimization</h4><p>Find out how we use predictive and prescriptive analytics to improve business performance</p><div class="go"><svg width="8" height="10" viewBox="0 0 8 10"><path d="M2 1l4 4-4 4" stroke="#fff" stroke-width="2" fill="none"/></svg></div></div>
    <div class="tech-card white" style="left:959px"><div class="tech-icon" role="img" aria-label="Icon of connected application windows" style="background:linear-gradient(180deg,#4aa0e0,#5cc08a)"></div><h4>Flexible<br>Architecture</h4><p>Find out how we use predictive and prescriptive analytics to improve business performance</p><div class="go"><svg width="8" height="10" viewBox="0 0 8 10"><path d="M2 1l4 4-4 4" stroke="#fff" stroke-width="2" fill="none"/></svg></div></div>
  </section>

  <!-- PARTNERS -->
  <section class="partners" aria-label="Clients">
    <svg class="abs" style="left:80px;top:106px" width="8" height="12" viewBox="0 0 8 12"><path d="M6 1 2 6l4 5" stroke="#fff" stroke-width="2" fill="none"/></svg>
    <div class="badge" style="left:158px;top:92px;width:64px;height:40px;border-radius:50%"></div>
    <div class="badge" style="left:344px;top:100px;width:88px;height:24px;border-radius:4px"></div>
    <div class="badge" style="left:560px;top:88px;width:48px;height:48px;transform:rotate(45deg)"></div>
    <div class="badge" style="left:724px;top:100px;width:148px;height:22px;border-radius:4px"></div>
    <div class="badge" style="left:936px;top:96px;width:120px;height:30px;border-radius:4px"></div>
    <svg class="abs" style="left:1100px;top:106px" width="8" height="12" viewBox="0 0 8 12"><path d="M2 1l4 5-4 5" stroke="#fff" stroke-width="2" fill="none"/></svg>
  </section>

  <!-- CONTACT -->
  <section class="contact">
    <h2 class="section-title" style="top:76px;font-size:27px;font-weight:700;color:#222">CONTACT US</h2>
    <div class="contact-item" style="left:144px">
      <svg width="20" height="26" viewBox="0 0 20 26"><path d="M2 1h11l5 5v19H2z" fill="#222"/><path d="M5 12h10M5 16h10M5 20h7" stroke="#fff" stroke-width="1.6"/></svg>Information Request
    </div>
    <div class="contact-item" style="left:460px">
      <svg width="32" height="24" viewBox="0 0 32 24"><rect x="5" y="2" width="22" height="15" rx="1" fill="none" stroke="#222" stroke-width="2.4"/><rect x="1" y="19" width="30" height="3" rx="1" fill="#222"/></svg>Ask for a demo
    </div>
    <div class="contact-item" style="left:754px">
      <svg width="28" height="28" viewBox="0 0 28 28"><path d="M4 16v-3a10 10 0 0 1 20 0v3" fill="none" stroke="#222" stroke-width="2.4"/><rect x="2" y="15" width="6" height="9" rx="2" fill="#222"/><rect x="20" y="15" width="6" height="9" rx="2" fill="#222"/></svg>Let us give you a call
    </div>

    <h3 class="links-title" style="left:75px;top:280px">QUICK LINKS</h3>
    <ul class="links" style="left:76px;top:328px"><li>Home</li><li>About Us</li><li>Industries</li><li>How we work</li></ul>
    <ul class="links" style="left:346px;top:328px"><li>Technologies</li><li>Testimonial</li><li>Contact</li></ul>

    <h3 class="links-title" style="left:915px;top:286px">FOLLOW US</h3>
    <div class="follow"><span></span><span></span><span></span><span></span></div>

    <div class="brand" style="left:802px;top:440px;font-size:66px">Resolva<span class="brand-dot" style="width:38px;height:38px"></span></div>
  </section>

  <footer class="footer">© 2019 &nbsp;|&nbsp; www.resolva-ai.example<span class="tag">M1</span></footer>
</div>
</body>
</html>
```